Business Card for a finance professional

I need a business card design to introduce myself to a professional networking (mainly banks) and potential companies to hire and remember me. I would like to use black, grey, white and maybe gold/silver colors and maybe something with my initials(R L F P T). The final design should communicate seriousness, profissionalism and something innovative.

The basic informations in the card are: Name, e-mail, phone number and trabnet. (I'm thinking to put some directly short link to my trabnet account or maybe some app - non QR Code - to add my contacts to a phone directly.)

My name is Mariana Lopes Ferreira Pinto dos Reis (I prefer to use only 'Mariana Lopes' or 'Mariana Reis' but i'm open to other suggestions) and I have 26 years old (just if it helps to build based in my age).
Updates

Dear designers, I wish to thank your participation in this project! It was very difficult to choose one! Thank your for your work! Best regards and success. Mariana

Target Market(s)

Potential hires and big companies.

Industry/Entity Type

Finance

Requirements
Must have
• The informations required at the business card are:
Name: Mariana Lopes F. P. dos Reis
Email: mariana.lop.reis@quellomail.com
Phone: +55 61 8493 5710
TrabNet: http://br.trabnet-perfis.com/in/marianalr/
Nice to have
• Modern and innovative look.
I suggest to use the colors black, grey, white, gold and/or silver, but I'm open to other colors.
Should not have
• A message showing that I need to be hired. It's more to "know me and remember me" than "hire me please".

```html
<!DOCTYPE html>
<html lang="en">
<head>
<meta charset="utf-8">
<title>Mariana Lopes F. P. dos Reis — Business Card</title>
<link rel="stylesheet" href="https://fonts.googleapis.com/css2?family=Roboto+Condensed:wght@700&family=Arimo&family=Questrial&display=swap">
<style>
  :root {
    --card-black: #000000;
    --glow-grey: #5a5a5a;
    --bar-light: #ffffff;
    --bar-mid: #b4b4b4;
    --bar-dark: #3a3a3a;
    --text-white: #ffffff;
    --name-shadow: #8c8c8c;
    --tile-phone: #ff00ff;
    --tile-email: #ffff00;
    --tile-profile: #151515;
    --tile-label-dark: #222222;
  }
  html, body {
    margin: 0;
    padding: 0;
    width: 1200px;
    height: 758px;
    overflow: hidden;
    background: var(--bar-light);
  }
  .card {
    position: relative;
    width: 1200px;
    height: 758px;
    overflow: hidden;
    background: var(--bar-light);
  }
  .edge-bar {
    position: absolute;
    left: 0;
    width: 1200px;
    height: 30px;
  }
  .edge-bar--top {
    top: 0;
    background: linear-gradient(to bottom, var(--bar-dark) 0%, var(--bar-mid) 45%, var(--bar-light) 100%);
  }
  .edge-bar--bottom {
    bottom: 0;
    height: 34px;
    background: linear-gradient(to bottom, var(--bar-light) 0%, var(--bar-mid) 50%, var(--bar-dark) 100%);
  }
  .panel {
    position: absolute;
    left: 3px;
    top: 31px;
    width: 1194px;
    height: 686px;
    background:
      radial-gradient(ellipse 520px 420px at 360px 290px, var(--glow-grey) 0%, #2a2a2a 40%, var(--card-black) 100%);
  }
  .panel__seam {
    position: absolute;
    left: 586px;
    top: 0;
    width: 1px;
    height: 100%;
    background: linear-gradient(to bottom, rgba(255,255,255,0.04), rgba(255,255,255,0.09), rgba(255,255,255,0.03));
  }
  .holder-name {
    position: absolute;
    left: 0;
    top: 92px;
    width: 1200px;
    margin: 0;
    text-align: center;
    font-family: "Roboto Condensed", "Arial Narrow", sans-serif;
    font-weight: 700;
    font-size: 84px;
    letter-spacing: -1px;
    color: var(--text-white);
    text-shadow: 2px 2px 0 #d0d0d0, 3px 3px 0 var(--name-shadow), 4px 5px 3px rgba(0,0,0,0.8);
  }
  .divider {
    position: absolute;
    left: 152px;
    top: 264px;
    width: 928px;
    height: 3px;
    background: linear-gradient(to right, rgba(255,255,255,0) 0%, rgba(255,255,255,0.5) 30%, #ffffff 70%, rgba(255,255,255,0.3) 100%);
  }
  .contact {
    position: absolute;
    left: 168px;
    width: 900px;
    height: 100px;
  }
  .contact--phone { top: 304px; }
  .contact--email { top: 433px; }
  .contact--profile { top: 553px; }
  .contact__tile {
    position: absolute;
    left: 0;
    top: 0;
    width: 104px;
    height: 99px;
    display: flex;
    align-items: center;
    justify-content: center;
    font-family: "Questrial", "Century Gothic", sans-serif;
    font-size: 20px;
    box-sizing: border-box;
  }
  .contact__tile--phone { background: var(--tile-phone); color: #f4d0f4; }
  .contact__tile--email { background: var(--tile-email); color: var(--tile-label-dark); }
  .contact__tile--profile {
    background: var(--tile-profile);
    color: var(--text-white);
    font-family: "Arimo", Arial, sans-serif;
    border-top: 12px solid #050505;
    border-right: 1px solid #3a3a3a;
    border-bottom: 1px solid #3a3a3a;
    padding-bottom: 8px;
  }
  .contact__value {
    position: absolute;
    top: 50%;
    transform: translateY(-50%);
    margin: 0;
    font-family: "Arimo", Arial, sans-serif;
    font-size: 33px;
    color: var(--text-white);
    white-space: nowrap;
  }
  .contact--phone .contact__value { left: 128px; }
  .contact--email .contact__value { left: 135px; }
  .contact--profile .contact__value { left: 135px; }
</style>
</head>
<body>
  <div class="card">
    <div class="edge-bar edge-bar--top"></div>
    <div class="panel">
      <div class="panel__seam"></div>
    </div>

    <h1 class="holder-name">Mariana Lopes F. P. dos Reis</h1>
    <div class="divider"></div>

    <div class="contact contact--phone">
      <div class="contact__tile contact__tile--phone">phone</div>
      <p class="contact__value">+55 61 8493 5710</p>
    </div>

    <div class="contact contact--email">
      <div class="contact__tile contact__tile--email">e-mail</div>
      <p class="contact__value">mariana.lop.reis@quellomail.com</p>
    </div>

    <div class="contact contact--profile">
      <div class="contact__tile contact__tile--profile">trabnet</div>
      <p class="contact__value">http://br.trabnet-perfis.com/in/marianalr/</p>
    </div>

    <div class="edge-bar edge-bar--bottom"></div>
  </div>
</body>
</html>
```